New business card for civil engineering company - "Keystone Audit"

We need a business card designed for our new structural engineering company.

The company name is "Keystone Audit" logo files attached.

We would like the following:
* Two-sided card
* Simple design

Information to be placed on the card:
Name - Marcus Dellow
Job Title - Director / Structural Engineer
Credentials - BEng(Hons), CPEng, CMengNZ, IntPE(NZ)
Email - marcus.dellow@keystoneaudit.co.nz
mobile - 0219364058
website - www.keystoneaudit.co.nz

```html
<!DOCTYPE html>
<html lang="en">
<head>
<meta charset="utf-8">
<title>Keystone Audit — Business Card</title>
<link rel="stylesheet" href="https://fonts.googleapis.com/css2?family=Jost:wght@400;500&family=Nunito+Sans:wght@800&family=Open+Sans:wght@400;700&display=swap">
<style>
  :root {
    --navy: #15426f;
    --navy-deep: #123c66;
    --sky: #009fe3;
    --pale: #bfdcf3;
    --ink: #1d1d1d;
    --text: #2a2a2a;
    --white: #ffffff;
    --rule: #222222;
  }
  * { margin: 0; padding: 0; box-sizing: border-box; }
  html, body { width: 1200px; height: 1200px; overflow: hidden; background: var(--white); }
  .canvas { position: relative; width: 1200px; height: 1200px; }

  .card { position: absolute; overflow: hidden; box-shadow: 6px 10px 14px rgba(0,0,0,0.35); }

  /* Front */
  .card-front { left: 153px; top: 68px; width: 895px; height: 510px; background: var(--navy); }
  .front-mark { position: absolute; left: 412px; top: 190px; width: 70px; height: 70px; background: var(--pale); }
  .front-name {
    position: absolute; left: 0; right: 0; top: 282px; text-align: center;
    font-family: 'Jost', sans-serif; font-weight: 500; font-size: 34px;
    letter-spacing: 3px; color: var(--white);
  }
  .front-tagline {
    position: absolute; left: 0; right: 0; top: 323px; text-align: center;
    font-family: 'Open Sans', sans-serif; font-size: 12.5px; letter-spacing: 3px; color: var(--white);
  }
  .front-band {
    position: absolute; left: 0; right: 0; top: 369px; height: 90px; background: var(--sky);
    display: flex; align-items: center; justify-content: center;
    font-family: 'Jost', sans-serif; font-weight: 500; font-size: 66px; color: var(--white);
    letter-spacing: 1px;
  }
  .web-strip {
    position: absolute; left: 0; right: 0; text-align: center;
    font-family: 'Open Sans', sans-serif; font-size: 20px; letter-spacing: 5px; color: var(--white);
  }
  .web-strip b { font-weight: 700; }
  .card-front .web-strip { top: 474px; }

  /* Back */
  .card-back { left: 152px; top: 623px; width: 896px; height: 512px; background: var(--white); }
  .back-mark { position: absolute; left: 174px; top: 150px; width: 70px; height: 70px; background: var(--pale); }
  .back-name {
    position: absolute; left: 0; width: 420px; top: 238px; text-align: center;
    font-family: 'Jost', sans-serif; font-weight: 500; font-size: 30px; letter-spacing: 2px; color: var(--ink);
  }
  .back-tagline {
    position: absolute; left: 0; width: 420px; top: 382px; text-align: center;
    font-family: 'Open Sans', sans-serif; font-size: 13.5px; letter-spacing: 3px; color: var(--ink);
  }
  .divider { position: absolute; left: 419px; top: 61px; width: 2px; height: 338px; background: var(--rule); }

  .person { position: absolute; left: 489px; top: 58px; width: 400px; }
  .person-name {
    font-family: 'Nunito Sans', sans-serif; font-weight: 800; font-size: 40px; color: var(--navy);
    line-height: 52px;
  }
  .person-role {
    margin-top: 12px; font-family: 'Open Sans', sans-serif; font-size: 20px; line-height: 29px; color: var(--text);
  }
  .person-rule {
    position: absolute; left: 489px; top: 229px; width: 326px; height: 2px;
    background: linear-gradient(90deg, #333 0%, #333 55%, rgba(51,51,51,0) 100%);
  }
  .contact-list { position: absolute; left: 489px; top: 274px; list-style: none; }
  .contact-item {
    display: flex; align-items: center; height: 42px;
    font-family: 'Open Sans', sans-serif; font-size: 19px; color: var(--text);
  }
  .contact-item svg { width: 26px; height: 26px; margin-right: 18px; flex: none; }
  .contact-item b { font-weight: 700; color: var(--ink); }
  .contact-phone { font-weight: 700; font-size: 20px; color: var(--ink); }
  .back-band { position: absolute; left: 0; right: 0; top: 449px; height: 44px; background: var(--navy-deep); }
  .card-back .web-strip { top: 459px; }
</style>
</head>
<body>
<main class="canvas">

  <section class="card card-front" aria-label="Card front">
    <div class="front-mark"></div>
    <div class="front-name">KEYSTONE AUDIT</div>
    <div class="front-tagline">PEER REVIEW SPECIALISTS</div>
    <div class="front-band">KEYSTONE AUDIT</div>
    <div class="web-strip">www.<b>keystoneaudit</b>.co.nz</div>
  </section>

  <section class="card card-back" aria-label="Card back">
    <div class="back-mark"></div>
    <div class="back-name" style="top:345px">KEYSTONE AUDIT</div>
    <div class="back-tagline">PEER REVIEW SPECIALISTS</div>
    <div class="divider"></div>

    <div class="person">
      <h1 class="person-name">Marcus Dellow</h1>
      <p class="person-role">Director / Structural Engineer<br>Credentials - BEng(Hons), CPEng,<br>CMengNZ, IntPE(NZ)</p>
    </div>
    <div class="person-rule"></div>

    <ul class="contact-list">
      <li class="contact-item">
        <svg viewBox="0 0 26 26" aria-hidden="true">
          <path d="M6 3 L10 3 L11.5 8 L9 10 C10.5 13.5 12.5 15.5 16 17 L18 14.5 L23 16 L23 20 C23 21.5 21.5 23 20 23 C11 22.5 3.5 15 3 6 C3 4.5 4.5 3 6 3 Z" fill="var(--navy)"/>
          <path d="M15 3.5 A8 8 0 0 1 22.5 11 M15 7 A4.5 4.5 0 0 1 19 11" stroke="var(--navy)" stroke-width="1.8" fill="none"/>
        </svg>
        <span class="contact-phone">0219364058</span>
      </li>
      <li class="contact-item">
        <svg viewBox="0 0 26 26" aria-hidden="true">
          <circle cx="13" cy="13" r="12" fill="var(--navy)"/>
          <rect x="7" y="9" width="12" height="9" rx="1" fill="var(--white)"/>
          <path d="M7 9.5 L13 14 L19 9.5" stroke="var(--navy)" stroke-width="1.4" fill="none"/>
        </svg>
        <span>marcus.<b>dellow@keystoneaudit</b>.co.nz</span>
      </li>
      <li class="contact-item">
        <svg viewBox="0 0 26 26" aria-hidden="true">
          <g stroke="var(--navy)" stroke-width="1.6" fill="none">
            <circle cx="13" cy="13" r="10.5"/>
            <ellipse cx="13" cy="13" rx="4.5" ry="10.5"/>
            <path d="M2.5 13 H23.5 M4.5 7.5 H21.5 M4.5 18.5 H21.5 M13 2.5 V23.5"/>
          </g>
        </svg>
        <span>www.<b>keystoneaudit</b>.co.nz</span>
      </li>
    </ul>

    <div class="back-band"></div>
    <div class="web-strip">www.<b>keystoneaudit</b>.co.nz</div>
  </section>

</main>
</body>
</html>
```